Business Card Design Project - bel soravin group

dear Sirs

we need business card design for our group ( BEL Soravin Group ) , i have got the Logo design of our group from pixel harbor in previous , so all need details relating to our group i think available with you, as well as the the chosen logo design

we hope to provide us with business card logo that to be appropaite and satisfactory to us .

thanks

note : logo design of our group is attached .
Updates

Reason: please extend the deadline of my project for additional 15 days because i didn't received appropriate design for our gruop yet . kindly beaware that i have received 77 design till now , supossed to send me 200-250 design at least . thanks

Target Market(s)

contents
-

name : Korvan EL Mistrani

position : Operation Manager

Industry/Entity Type

Business

Requirements
Must have

• person name

group logo
Nice to have
• logo color matching with back background

```html
<!DOCTYPE html>
<html lang="en">
<head>
<meta charset="utf-8">
<title>BEL Soravin Group – Business Card</title>
<link rel="stylesheet" href="https://fonts.googleapis.com/css2?family=Open+Sans:wght@400;600&display=swap">
<style>
  :root {
    --navy: #1c3f7e;
    --navy-deep: #132d5e;
    --navy-light: #2a5aa6;
    --gold: #c9a347;
    --ink: #3c3c3c;
    --paper: #ffffff;
    --backdrop: #efe9d6;
  }
  html, body {
    margin: 0;
    padding: 0;
    width: 1200px;
    height: 951px;
    overflow: hidden;
    background: var(--backdrop);
    font-family: "Open Sans", sans-serif;
  }
  .stage {
    position: relative;
    width: 1200px;
    height: 951px;
  }
  .card {
    position: absolute;
    width: 580px;
    height: 330px;
    border-radius: 22px;
    overflow: hidden;
    box-shadow: 0 6px 18px rgba(0,0,0,0.18);
  }
  /* Back side */
  .card-back {
    left: 80px;
    top: 110px;
    background: radial-gradient(ellipse at 45% 45%, var(--navy-light) 0%, var(--navy) 55%, var(--navy-deep) 100%);
    color: var(--paper);
  }
  .card-back .brand {
    position: absolute;
    left: 0;
    right: 0;
    top: 100px;
    display: flex;
    align-items: center;
    justify-content: center;
    gap: 14px;
  }
  .brand-mark {
    width: 14px;
    height: 14px;
    background: currentColor;
  }
  .brand-text {
    font-weight: 600;
    line-height: 1;
    text-align: left;
  }
  .card-back .brand-name { font-size: 50px; letter-spacing: 1px; }
  .card-back .brand-sub { font-size: 20px; letter-spacing: 1px; margin-top: 6px; }
  .card-back .website {
    position: absolute;
    left: 0;
    right: 0;
    top: 228px;
    text-align: center;
    color: var(--gold);
    font-size: 17px;
    letter-spacing: 2px;
  }
  /* Front side */
  .card-front {
    left: 540px;
    top: 500px;
    background: var(--paper);
    color: var(--ink);
  }
  .card-front .brand {
    position: absolute;
    left: 40px;
    top: 40px;
    display: flex;
    align-items: center;
    gap: 10px;
    color: var(--navy);
  }
  .card-front .brand-name { font-size: 36px; letter-spacing: 0.5px; }
  .card-front .brand-sub { font-size: 14px; letter-spacing: 0.5px; margin-top: 4px; }
  .person {
    position: absolute;
    left: 365px;
    top: 58px;
  }
  .person-name { font-size: 17px; font-weight: 600; color: var(--ink); }
  .person-role { font-size: 14px; color: var(--gold); margin-top: 2px; }
  .contacts {
    position: absolute;
    left: 70px;
    top: 140px;
    list-style: none;
    margin: 0;
    padding: 0;
    font-size: 14px;
    line-height: 19px;
  }
  .contacts li { display: flex; align-items: center; gap: 8px; }
  .contacts svg { width: 12px; height: 12px; fill: var(--gold); }
  .contacts .accent { color: var(--gold); }
  .address {
    position: absolute;
    left: 275px;
    top: 160px;
    display: flex;
    gap: 8px;
    font-size: 14px;
    line-height: 19px;
  }
  .address svg { width: 13px; height: 13px; fill: var(--gold); margin-top: 2px; }
  .footer-rule {
    position: absolute;
    left: 0;
    right: 0;
    bottom: 46px;
    height: 6px;
    background: var(--gold);
  }
  .footer-band {
    position: absolute;
    left: 0;
    right: 0;
    bottom: 0;
    height: 40px;
    background: var(--navy);
  }
</style>
</head>
<body>
<main class="stage">

  <section class="card card-back" aria-label="Business card back">
    <div class="brand">
      <span class="brand-mark" aria-hidden="true"></span>
      <div class="brand-text">
        <div class="brand-name">BEL SORAVIN</div>
        <div class="brand-sub">GROUP OF COMPANIES</div>
      </div>
    </div>
    <div class="website">www.belsoravingroup.com</div>
  </section>

  <section class="card card-front" aria-label="Business card front">
    <div class="brand">
      <span class="brand-mark" aria-hidden="true"></span>
      <div class="brand-text">
        <div class="brand-name">BEL SORAVIN</div>
        <div class="brand-sub">GROUP OF COMPANIES</div>
      </div>
    </div>

    <div class="person">
      <div class="person-name">Korvan EL Mistrani</div>
      <div class="person-role">Operation Manager</div>
    </div>

    <ul class="contacts">
      <li>
        <svg viewBox="0 0 12 12" aria-hidden="true"><path d="M2.5 1 L4.5 1 L5 3.5 L3.8 4.5 C4.5 6 6 7.5 7.5 8.2 L8.5 7 L11 7.5 L11 9.5 C11 10.3 10.3 11 9.5 11 C5 11 1 7 1 2.5 C1 1.7 1.7 1 2.5 1 Z"/></svg>
        <span>555-014-2730</span>
      </li>
      <li>
        <svg viewBox="0 0 12 12" aria-hidden="true"><path d="M3 1 H9 V4 H3 Z M1 4.5 H11 V9 H9 V11 H3 V9 H1 Z M4 8 V10 H8 V8 Z"/></svg>
        <span>555-014-2731</span>
      </li>
      <li>
        <svg viewBox="0 0 12 12" aria-hidden="true"><path d="M1 3 H11 V10 H1 Z M1.5 3.3 L6 7 L10.5 3.3" stroke="#fff" stroke-width="0.8"/></svg>
        <span>info@<span class="accent">belsoravingroup</span>.com</span>
      </li>
      <li>
        <svg viewBox="0 0 12 12" aria-hidden="true"><circle cx="6" cy="6" r="5"/></svg>
        <span>www.<span class="accent">belsoravingroup</span>.com</span>
      </li>
    </ul>

    <div class="address">
      <svg viewBox="0 0 12 12" aria-hidden="true"><path d="M6 1 L11.5 6 H10 V11 H7.3 V8 H4.7 V11 H2 V6 H0.5 Z"/></svg>
      <div>4150 Marlow Crest Rd.<br>Suite 208-314<br>Delvin, TX 78114</div>
    </div>

    <div class="footer-rule" aria-hidden="true"></div>
    <div class="footer-band" aria-hidden="true"></div>
  </section>

</main>
</body>
</html>
```